BrightLoop App Design

The attached document, [BrightLoop - Design & Requirements Document - v1.2], outlines the full design and functional requirements for the BrightLoop App. The key sections include:
• Company overview: Mission and vision statements
• High-level application overview
• App design guidelines
• App functional requirements
• Navigation information
To expedite app development, we are planning to use a Multi-Purpose PWA Mobile App Template. This template offers pre-built UI elements and layouts that are flexible and responsive, allowing for quicker development while maintaining a modern design.
Pixel Harbor Requirements:
We require designs for 11 app pages and 1 pop-up, as outlined in sections 3.13 and section 4 of the document. These designs should be delivered in Adobe format (as a minimum), ready to be handed over to our developers who will build the app using the template and corresponding code base.
Important Notes:
1. Leverage the Multi-Purpose PWA Mobile App Template: The designs must make use of the components and features available within the template. You can explore the template using the following link to view the pages, features, and styles:
o Template link: Varn: Multi-Purpose PWA Mobile App Template
2. Sample screens for Visual Reference: To aid in visualizing the app's navigation, please refer to the sample screens. This serves as a high-level guide to demonstrate the user flow but is not a literal requirement for the design.
o Note:
 Not all features and pages from the requirements document are represented in these screen samples
 The flow is provided purely to showcase the navigational paths within the app.

Deliverables:
The designs should align with the template's style, features, and UI components, with clear attention to how each page will function within the BrightLoop app. The final designs are expected to be in Adobe format for smooth developer handoff.
To confirm, we are looking to see how best to utilise the template design style etc for the APP’s final design, whilst incorporating all the requirements of the APP from the requirements document.

Target Market(s)

Young shopping demographic

Industry/Entity Type

Online Shopping

Requirements
Must have
• All the required pages designed
Nice to have
• See requirements document

```html
<!DOCTYPE html>
<html lang="en">
<head>
<meta charset="utf-8">
<title>BrightLoop App Screens</title>
<link href="https://fonts.googleapis.com/css2?family=Lato:wght@400;700;900&display=swap" rel="stylesheet">
<style>
:root{
  --bg:#262626;
  --teal:#26a69a;
  --teal-dark:#1e8c82;
  --teal-soft:#e3f4f2;
  --ink:#333;
  --muted:#8a8a8a;
  --faint:#b5b5b5;
  --line:#dcdcdc;
  --red:#f06262;
  --orange:#f5a623;
  --pink:#ee3f7f;
  --white:#fff;
}
*{box-sizing:border-box;margin:0;padding:0}
html,body{width:1200px;height:2835px;overflow:hidden;background:var(--bg);font-family:'Lato',sans-serif;color:var(--ink)}
.screen{position:absolute;width:279px;background:var(--white);overflow:hidden}
.screen *{position:absolute}
.screen .flow,.screen .flow *{position:static}
.title{left:0;width:100%;text-align:center;font-size:14px;font-weight:700;color:#555;letter-spacing:.3px}
.lead{left:30px;width:219px;text-align:center;font-size:8.5px;line-height:12.5px;color:var(--muted)}
.field{left:42px;width:194px;height:33px;border:1px solid var(--line);border-radius:17px;font-size:10.5px;color:var(--faint);padding-left:14px;line-height:31px}
.btn{height:33px;border-radius:17px;background:var(--teal);color:var(--white);font-size:10.5px;font-weight:700;text-align:center;line-height:33px;letter-spacing:.2px}
.small{font-size:8.5px;color:var(--muted);left:0;width:100%;text-align:center}
.rule{height:1px;background:var(--line)}
.social{left:52px;width:174px;height:47px;border:1px solid var(--teal);border-radius:3px}
.social .mark{left:24px;top:14px;width:18px;height:18px;border-radius:50%;background:#444}
.social span{left:74px;top:11px;font-size:10.5px;line-height:12px;color:#444;letter-spacing:.3px}
.hdr{left:0;top:0;width:100%;background:var(--teal)}
.hdr-title{left:21px;top:50px;color:var(--white);font-size:14px;font-weight:700;letter-spacing:.3px}
.hdr-title::after{content:"";position:absolute;left:0;top:22px;width:44px;height:2px;background:var(--white)}
.back{left:19px;top:16px;width:12px;height:14px}
.card-top{left:0;width:100%;background:var(--white);border-radius:22px 22px 0 0}
.logobar{left:0;top:0;width:100%;height:40px;background:var(--white)}
.logobar .brand{left:0;width:100%;top:9px;text-align:center;font-size:17px;font-weight:900;color:var(--ink)}
.logobar .back{top:13px;left:17px}
.logobar .user{right:20px;top:11px;width:18px;height:18px}
.label{left:21px;font-size:8.5px;font-weight:700;color:#555}
.nav{left:0;width:100%;height:58px;background:var(--white);border-radius:20px 20px 0 0;box-shadow:0 -2px 8px rgba(0,0,0,.06)}
.nav .item{width:90px;text-align:center;font-size:8.5px;color:#666;top:37px}
.nav .item.on{color:var(--teal)}
.nav svg{width:16px;height:16px}
.nav .bubble{width:32px;height:32px;border-radius:50%;background:var(--teal);top:-8px;box-shadow:0 2px 5px rgba(0,0,0,.15)}
.nav .bubble svg{left:8px;top:8px}
.toggle{left:50px;width:178px;height:33px;border-radius:17px;background:#f1f1f1}
.toggle span{top:0;width:89px;height:33px;line-height:33px;text-align:center;font-size:10.5px;color:#666}
.toggle span.on{background:var(--teal);color:var(--white);border-radius:17px;font-weight:700}
.tile{width:107px;height:112px;border-radius:12px;background:#f3f3f3;text-align:center}
.tile svg{left:41px;top:32px;width:24px;height:24px}
.tile span{left:0;width:100%;top:70px;font-size:8.5px;color:#666}
.photo{background:linear-gradient(160deg,#d9dcdc,#a7abac 55%,#6d7172)}
.photo-shoe{background:linear-gradient(160deg,#f1f1f1,#bdbdbd 60%,#3a3a3a)}
.chip{height:20px;border-radius:10px;background:#eee;font-size:9.5px;color:#666;text-align:center;line-height:20px}
.chip.on{background:var(--teal);color:var(--white)}
.pcard{width:110px;height:182px;background:#f6f6f6;border-radius:4px;overflow:hidden}
.pcard .img{left:0;top:0;width:110px;height:110px}
.pcard .corner{left:0;top:0;width:0;height:0;border-top:24px solid var(--teal);border-right:24px solid transparent}
.pcard .plus{left:76px;top:78px;width:26px;height:26px;border-radius:50%;background:var(--teal)}
.pcard .name{left:9px;top:121px;font-size:10.5px;color:#444}
.pcard .off{left:9px;top:138px;font-size:8.5px;color:var(--faint)}
.pcard .off.hot{color:#f07a5a}
.pcard .price{left:9px;top:155px;font-size:14px;font-weight:900;color:var(--teal)}
.pcard .price s{font-size:8px;font-weight:400;color:var(--faint);margin-left:4px}
.section{left:21px;font-size:13.5px;font-weight:700;color:var(--teal)}
.pill{height:16px;border-radius:8px;color:var(--white);font-size:8px;line-height:16px;padding-left:22px}
.pill i{position:absolute;left:8px;top:4px;width:8px;height:8px;border-radius:50%;background:rgba(255,255,255,.85)}
.size{top:419px;width:36px;height:16px;border:1px solid var(--line);border-radius:8px;font-size:8px;color:#888;text-align:center;line-height:14px}
.dot{top:450px;width:17px;height:17px;border-radius:50%}
.para{left:21px;width:237px;font-size:8.5px;line-height:17px;color:#9a9a9a}
.cart-row{left:0;width:100%;height:52px}
.cart-row .thumb{left:21px;top:0;width:33px;height:33px;border-radius:50%;background:linear-gradient(135deg,#c9c9c9,#555)}
.cart-row .nm{left:62px;top:-2px;font-size:14px;font-weight:700;color:var(--teal)}
.cart-row .meta{left:62px;top:19px;font-size:7.5px;font-style:italic;color:var(--faint)}
.cart-row .amt{left:191px;top:5px;width:65px;height:22px;border-radius:11px;background:var(--teal-soft);color:var(--teal);font-size:10px;text-align:center;line-height:22px}
.tag{height:20px;border-radius:10px;background:var(--white);font-size:8.5px;color:#444;padding:0 8px;line-height:20px;box-shadow:0 1px 3px rgba(0,0,0,.2)}
.tag-box{border:1.5px dashed rgba(255,255,255,.85);border-radius:8px}
.quick{top:509px;height:26px;border-radius:13px;background:#eee;font-size:8px;color:#999;line-height:26px;padding:0 15px;white-space:nowrap}
</style>
</head>
<body>

<!-- ROW 1 -->
<section class="screen" style="left:22px;top:22px;height:603px">
  <div class="title" style="top:73px">REGISTER</div>
  <div class="field" style="top:129px">Name</div>
  <div class="field" style="top:183px">Email</div>
  <div class="field" style="top:236px">Password</div>
  <div class="btn" style="left:77px;top:315px;width:123px">REGISTER</div>
  <div class="small" style="top:359px">Already Registeres? Login</div>
  <div class="rule" style="left:31px;top:389px;width:216px"></div>
  <div class="social" style="top:409px"><div class="mark"></div><span>Register&nbsp; With<br>Nimbus</span></div>
  <div class="social" style="top:466px"><div class="mark"></div><span>Register&nbsp; With<br>Orchard</span></div>
</section>

<section class="screen" style="left:315px;top:22px;height:603px">
  <div class="title" style="top:73px">SIGN-IN</div>
  <div class="field" style="top:127px">Email</div>
  <div class="field" style="top:180px">Password</div>
  <div style="left:42px;top:226px;width:16px;height:16px;border:1px solid var(--teal);border-radius:3px"></div>
  <div style="left:66px;top:229px;font-size:8.5px;color:#666">Remember me</div>
  <div class="small" style="top:288px;color:#666">Forgot Password &nbsp;&nbsp;|&nbsp;&nbsp; Register</div>
  <div class="btn" style="left:77px;top:325px;width:123px">SIGN-IN</div>
  <div class="btn" style="left:77px;top:370px;width:123px">SIGN-IN AS GUEST</div>
  <div class="rule" style="left:31px;top:424px;width:216px"></div>
  <div class="social" style="top:443px"><div class="mark"></div><span>Register&nbsp; With<br>Nimbus</span></div>
  <div class="social" style="top:500px"><div class="mark"></div><span>Register&nbsp; With<br>Orchard</span></div>
</section>

<section class="screen" style="left:607px;top:22px;height:603px">
  <div class="title" style="top:73px">CHANGE PASSWORD</div>
  <div class="lead" style="top:98px">Lorem ipsum odor amet, consectetuer adipiscing elit. Suspendisse eleifend rhoncus nulla dictum proin interdum.</div>
  <div class="field" style="top:164px">Email</div>
  <div class="small" style="top:229px;color:#666">Login &nbsp;&nbsp;|&nbsp;&nbsp; Register</div>
  <div class="btn" style="left:76px;top:262px;width:126px">RESET PASSWORD</div>
</section>

<section class="screen" style="left:900px;top:22px;height:603px">
  <div class="title" style="top:73px">CHANGE PASSWORD</div>
  <div class="lead" style="top:98px">Lorem ipsum odor amet, consectetuer adipiscing elit. Suspendisse eleifend rhoncus nulla dictum proin interdum.</div>
  <div class="btn" style="left:75px;top:164px;width:127px">BACK TO LOGIN</div>
  <svg style="left:80px;top:207px;width:11px;height:11px" viewBox="0 0 12 12"><circle cx="6" cy="6" r="4.5" fill="none" stroke="#e5e5e5" stroke-width="2"/><path d="M6 1.5A4.5 4.5 0 0 1 10.5 6" fill="none" stroke="var(--teal)" stroke-width="2"/></svg>
  <div style="left:99px;top:207px;font-size:8.5px;color:#666">Back to login page in 5s</div>
</section>

<!-- ROW 2 -->
<section class="screen" style="left:22px;top:640px;height:604px">
  <div class="hdr" style="height:175px"></div>
  <svg class="back" viewBox="0 0 12 14"><path d="M8 3L4 7l4 4" stroke="#fff" stroke-width="2" fill="none"/></svg>
  <svg style="left:34px;top:19px;width:12px;height:12px" viewBox="0 0 12 12"><path d="M1 3h10M1 6h7M1 9h10" stroke="#fff" stroke-width="1.6"/></svg>
  <div class="hdr-title" style="top:48px">PROFILE</div>
  <div class="card-top" style="top:152px;height:452px"></div>
  <div role="img" aria-label="Profile photo of the user" style="left:80px;top:93px;width:118px;height:118px;border-radius:50%;background:radial-gradient(circle at 50% 45%,#b0624f,#7a3326 55%,#e06b86 90%)"></div>
  <div class="title" style="top:226px;font-size:14px">NAME</div>
  <div class="label" style="top:264px">EMAIL</div>
  <div class="field" style="left:30px;width:218px;top:279px">Email</div>
  <div class="label" style="top:328px">ADDRESS</div>
  <div class="field" style="left:30px;width:218px;top:344px">Address 1, State, Country, ZIP</div>
  <div class="label" style="top:392px">DATE OF BIRTH</div>
  <div class="field" style="left:30px;width:218px;top:407px">MM-DD-YYYY</div>
  <div class="label" style="top:456px">PASSWORD</div>
  <div class="field" style="left:30px;width:218px;top:470px">********</div>
  <div class="btn" style="left:75px;top:549px;width:126px">&#8680;&nbsp; LOGOUT</div>
</section>

<section class="screen" style="left:315px;top:640px;height:604px">
  <div class="hdr" style="top:40px;height:120px"></div>
  <div class="logobar"><svg class="back" viewBox="0 0 12 14"><path d="M8 3L4 7l4 4" stroke="#222" stroke-width="2" fill="none"/></svg><div class="brand">BrightLoop</div><svg class="user" viewBox="0 0 18 18"><circle cx="9" cy="9" r="8" fill="none" stroke="#222" stroke-width="2"/><circle cx="9" cy="7.5" r="3" fill="#222"/><path d="M4 14c2-3 8-3 10 0" fill="#222"/></svg></div>
  <div class="hdr-title">SEARCH</div>
  <div class="card-top" style="top:95px;height:509px"></div>
  <div class="toggle" style="top:132px"><span class="on" style="left:0">IMAGE</span><span style="left:89px">TEXT</span></div>
  <div class="lead" style="top:196px">Provide an image of any fashion item and we'll create a personalized set of recommendations for you</div>
  <div class="tile" style="left:25px;top:257px"><svg viewBox="0 0 24 24"><rect x="3" y="4" width="18" height="16" rx="2" fill="none" stroke="var(--teal)" stroke-width="1.6"/><path d="M5 17l5-5 3 3 2-2 4 4" stroke="var(--teal)" stroke-width="1.6" fill="none"/></svg><span>Upload an Image</span></div>
  <div class="tile" style="left:146px;top:257px"><svg viewBox="0 0 24 24"><rect x="2" y="6" width="20" height="15" rx="3" fill="var(--teal)"/><rect x="8" y="3" width="8" height="4" rx="1" fill="var(--teal)"/><circle cx="12" cy="13.5" r="4" fill="#fff"/><path d="M12 11.5v4M10 13.5h4" stroke="var(--teal)" stroke-width="1.4"/></svg><span>Take a Photo</span></div>
  <div class="nav" style="top:546px">
    <div class="bubble" style="left:39px"><svg viewBox="0 0 16 16"><circle cx="7" cy="7" r="4.5" fill="none" stroke="#fff" stroke-width="2"/><path d="M10.5 10.5L14 14" stroke="#fff" stroke-width="2"/></svg></div>
    <div class="item on" style="left:10px">Search</div>
    <svg style="left:132px;top:11px" viewBox="0 0 16 16"><path d="M8 1l1.5 4.5L14 7l-4.5 1.5L8 13 6.5 8.5 2 7l4.5-1.5z" fill="#444"/></svg>
    <div class="item" style="left:95px">Recommendations</div>
    <svg style="left:216px;top:11px" viewBox="0 0 16 16"><path d="M1 2h2.5l2 8h7l2-6H5" fill="none" stroke="#444" stroke-width="1.6"/><circle cx="6.5" cy="13" r="1.4" fill="#444"/><circle cx="11.5" cy="13" r="1.4" fill="#444"/></svg>
    <div class="item" style="left:179px">Cart</div>
  </div>
</section>

<section class="screen" style="left:607px;top:640px;height:604px">
  <div class="hdr" style="top:40px;height:120px"></div>
  <div class="logobar"><svg class="back" viewBox="0 0 12 14"><path d="M8 3L4 7l4 4" stroke="#222" stroke-width="2" fill="none"/></svg><div class="brand">BrightLoop</div><svg class="user" viewBox="0 0 18 18"><circle cx="9" cy="9" r="8" fill="none" stroke="#222" stroke-width="2"/><circle cx="9" cy="7.5" r="3" fill="#222"/><path d="M4 14c2-3 8-3 10 0" fill="#222"/></svg></div>
  <div class="hdr-title">SEARCH</div>
  <div class="card-top" style="top:95px;height:509px"></div>
  <div class="toggle" style="top:132px"><span style="left:0">IMAGE</span><span class="on" style="left:89px">TEXT</span></div>
  <div class="lead" style="top:196px">Describe below your desired fashion item and select any filter that suits your needs</div>
  <div style="left:19px;top:234px;width:241px;height:32px;border-radius:16px;background:#f1f1f1;font-size:10.5px;color:var(--faint);line-height:32px;padding-left:30px">Describe your fashion item</div>
  <svg style="left:32px;top:245px;width:10px;height:10px" viewBox="0 0 10 10"><circle cx="4" cy="4" r="3" fill="none" stroke="#bbb" stroke-width="1.3"/><path d="M6.3 6.3L9 9" stroke="#bbb" stroke-width="1.3"/></svg>
  <div style="left:19px;top:291px;font-size:10.5px;color:#888">Price</div>
  <div class="chip" style="left:67px;top:288px;width:44px">&lt; 50</div>
  <div class="chip on" style="left:117px;top:288px;width:44px">&gt; 75</div>
  <div class="chip" style="left:167px;top:288px;width:44px">&lt; 100</div>
  <div class="chip" style="left:217px;top:288px;width:44px">&gt; 200</div>
  <div style="left:19px;top:334px;font-size:8.5px;color:#888">Only show products eligible for free shipping</div>
  <div style="left:214px;top:327px;width:46px;height:24px;border-radius:12px;background:var(--teal)"><div style="left:25px;top:3px;width:18px;height:18px;border-radius:50%;background:#fff"></div></div>
  <div class="nav" style="top:546px">
    <div class="bubble" style="left:39px"><svg viewBox="0 0 16 16"><circle cx="7" cy="7" r="4.5" fill="none" stroke="#fff" stroke-width="2"/><path d="M10.5 10.5L14 14" stroke="#fff" stroke-width="2"/></svg></div>
    <div class="item on" style="left:10px">Search</div>
    <svg style="left:132px;top:11px" viewBox="0 0 16 16"><path d="M8 1l1.5 4.5L14 7l-4.5 1.5L8 13 6.5 8.5 2 7l4.5-1.5z" fill="#444"/></svg>
    <div class="item" style="left:95px">Recommendations</div>
    <svg style="left:216px;top:11px" viewBox="0 0 16 16"><path d="M1 2h2.5l2 8h7l2-6H5" fill="none" stroke="#444" stroke-width="1.6"/><circle cx="6.5" cy="13" r="1.4" fill="#444"/><circle cx="11.5" cy="13" r="1.4" fill="#444"/></svg>
    <div class="item" style="left:179px">Cart</div>
  </div>
</section>

<section class="screen" style="left:900px;top:640px;height:604px">
  <div class="hdr" style="height:140px"></div>
  <svg class="back" viewBox="0 0 12 14"><path d="M8 3L4 7l4 4" stroke="#fff" stroke-width="2" fill="none"/></svg>
  <div class="hdr-title">SEARCH</div>
  <div class="card-top" style="top:95px;height:509px"></div>
  <div class="photo" role="img" aria-label="Uploaded photo of a woman in sporty outfit crouching" style="left:59px;top:166px;width:159px;height:270px;border-radius:6px"></div>
  <svg style="left:80px;top:475px;width:11px;height:11px" viewBox="0 0 12 12"><circle cx="6" cy="6" r="4.5" fill="none" stroke="#e5e5e5" stroke-width="2"/><path d="M6 1.5A4.5 4.5 0 0 1 10.5 6" fill="none" stroke="var(--teal)" stroke-width="2"/></svg>
  <div style="left:99px;top:474px;font-size:10.5px;color:#333">Scanning Image</div>
  <div class="lead" style="top:504px;font-size:8px;line-height:10px">One moment while we analyse the image to identify the clothing item</div>
</section>

<!-- ROW 3 -->
<section class="screen" style="left:22px;top:1258px;height:604px">
  <div class="hdr" style="height:140px"></div>
  <svg class="back" viewBox="0 0 12 14"><path d="M8 3L4 7l4 4" stroke="#fff" stroke-width="2" fill="none"/></svg>
  <div class="hdr-title">SEARCH</div>
  <div class="card-top" style="top:92px;height:512px"></div>
  <div class="photo" role="img" aria-label="Uploaded photo with detected clothing areas" style="left:59px;top:166px;width:159px;height:270px;border-radius:6px"></div>
  <div class="tag-box" style="left:90px;top:232px;width:95px;height:44px"></div>
  <div class="tag-box" style="left:90px;top:280px;width:120px;height:56px"></div>
  <div class="tag-box" style="left:90px;top:360px;width:95px;height:38px"></div>
  <div class="tag" style="left:132px;top:248px">Top</div>
  <div class="tag" style="left:171px;top:292px">Bottom</div>
  <div class="tag" style="left:143px;top:363px">Shoes</div>
  <div class="lead" style="top:477px;font-size:8px;line-height:10px">Select the item of clothing you wish to search for</div>
</section>

<section class="screen" style="left:315px;top:1258px;height:936px">
  <div class="hdr" style="top:40px;height:120px"></div>
  <div class="logobar"><svg class="back" viewBox="0 0 12 14"><path d="M8 3L4 7l4 4" stroke="#222" stroke-width="2" fill="none"/></svg><div class="brand">BrightLoop</div><svg class="user" viewBox="0 0 18 18"><circle cx="9" cy="9" r="8" fill="none" stroke="#222" stroke-width="2"/><circle cx="9" cy="7.5" r="3" fill="#222"/><path d="M4 14c2-3 8-3 10 0" fill="#222"/></svg></div>
  <div class="hdr-title">FOR YOU</div>
  <div class="card-top" style="top:92px;height:844px"></div>
  <div role="img" aria-label="Promotional banner photo of a woman with flowers on yellow" style="left:21px;top:120px;width:235px;height:170px;border-radius:6px;background:linear-gradient(120deg,#f7b81c,#f4a51a 60%,#ee9b18)"></div>
  <div style="left:110px;top:210px;font-size:20px;font-weight:900;color:#fff;line-height:26px;opacity:.9">PROMOTE<br>HERE</div>
  <div style="left:119px;top:274px;width:14px;height:5px;border-radius:3px;background:#fff"></div>
  <div style="left:137px;top:274px;width:5px;height:5px;border-radius:50%;background:rgba(255,255,255,.7)"></div>
  <div style="left:146px;top:274px;width:5px;height:5px;border-radius:50%;background:rgba(255,255,255,.7)"></div>
  <div style="left:21px;top:314px;font-size:13.5px;font-weight:700;color:#444">20 PRODUCTS</div>
  <svg style="left:238px;top:314px;width:16px;height:17px" viewBox="0 0 16 17"><path d="M1 1h14l-5.5 7v7l-3-2V8z" fill="none" stroke="var(--teal)" stroke-width="1.6"/></svg>
  <div class="section" style="top:355px">DIRECT MATCH</div>
  <div class="pcard" style="left:21px;top:403px"><div class="img photo" role="img" aria-label="Product photo"></div><div class="corner"></div><div class="plus"></div><div class="name">PRODUCT ITEM</div><div class="off">30% OFF</div><div class="price">$18.99<s>$18.99</s></div></div>
  <div class="pcard" style="left:146px;top:403px"><div class="img photo" role="img" aria-label="Product photo"></div><div class="corner"></div><div class="plus"></div><div class="name">PRODUCT ITEM</div><div class="off">30% OFF</div><div class="price">$18.99<s>$18.99</s></div></div>
  <div class="section" style="top:621px">SIMILAR ITEMS</div>
  <div class="pcard" style="left:21px;top:670px"><div class="img photo-shoe" role="img" aria-label="Sneaker product photo"></div><div class="corner"></div><div class="plus"></div><div class="name">PRODUCT ITEM</div><div class="off hot">30% OFF</div><div class="price">$18.99<s>$18.99</s></div></div>
  <div class="pcard" style="left:146px;top:670px"><div class="img photo-shoe" role="img" aria-label="Sneaker product photo"></div><div class="corner"></div><div class="plus"></div><div class="name">PRODUCT ITEM</div><div class="off hot">30% OFF</div><div class="price">$18.99<s>$18.99</s></div></div>
  <div class="nav" style="top:878px">
    <svg style="left:47px;top:11px" viewBox="0 0 16 16"><circle cx="7" cy="7" r="4.5" fill="none" stroke="#444" stroke-width="2"/><path d="M10.5 10.5L14 14" stroke="#444" stroke-width="2"/></svg>
    <div class="item" style="left:10px">Search</div>
    <div class="bubble" style="left:124px"><svg viewBox="0 0 16 16"><path d="M8 1l1.5 4.5L14 7l-4.5 1.5L8 13 6.5 8.5 2 7l4.5-1.5z" fill="#fff"/></svg></div>
    <div class="item on" style="left:95px">Recommendations</div>
    <svg style="left:216px;top:11px" viewBox="0 0 16 16"><path d="M1 2h2.5l2 8h7l2-6H5" fill="none" stroke="#444" stroke-width="1.6"/><circle cx="6.5" cy="13" r="1.4" fill="#444"/><circle cx="11.5" cy="13" r="1.4" fill="#444"/></svg>
    <div class="item" style="left:179px">Cart</div>
  </div>
</section>

<section class="screen" style="left:607px;top:1258px;height:781px">
  <div class="hdr" style="height:140px"></div>
  <svg class="back" viewBox="0 0 12 14"><path d="M8 3L4 7l4 4" stroke="#fff" stroke-width="2" fill="none"/></svg>
  <div class="hdr-title">PRODUCT DETAILS</div>
  <div class="card-top" style="top:92px;height:689px"></div>
  <div class="photo" role="img" aria-label="Product photo of a woman in sporty outfit" style="left:21px;top:120px;width:235px;height:170px"></div>
  <div style="left:21px;top:311px;font-size:14px;color:#333">PRODUCT ITEM</div>
  <div class="pill" style="left:21px;top:334px;width:72px;background:var(--red)"><i></i>30% OFF</div>
  <div class="pill" style="left:101px;top:334px;width:96px;background:var(--teal)"><i></i>Free Shipping</div>
  <div class="pill" style="left:21px;top:358px;width:70px;background:var(--orange)"><i></i>Returns</div>
  <div style="left:21px;top:386px;font-size:14px;font-weight:900;color:var(--teal)">$18.99 <span style="position:static;font-size:8px;font-weight:400;color:var(--faint);text-decoration:line-through">$18.99</span></div>
  <div class="size" style="left:23px">S</div><div class="size" style="left:65px">M</div><div class="size" style="left:107px">L</div><div class="size" style="left:149px">XL</div>
  <div class="dot" style="left:23px;background:var(--red)"></div><div class="dot" style="left:46px;background:#7fd1c7"></div><div class="dot" style="left:69px;background:#3d4a5c"></div>
  <div class="para" style="top:480px">Lorem ipsum odor amet, consectetuer adipiscing elit. Habitasse neque rhoncus lobortis vehicula hendrerit vel dapibus. Urna cursus facilisis senectus pulvinar neque laoreet venenatis. Ex feugiat felis fermentum laoreet class semper? Orci aliquam nulla mus sapien lorem porttitor venenatis nisi quisque. Eleifend elementum sem efficitur lobortis arcu. Turpis ridiculus vestibulum; faucibus adipiscing morbi at platea dictum.</div>
  <div style="left:21px;top:646px;width:235px;height:61px;border:1px solid #eee;border-radius:6px">
    <div style="left:12px;top:12px;width:36px;height:36px;border-radius:50%;background:var(--teal)"></div>
    <div style="left:60px;top:11px;font-size:12px;color:#333">Store Name</div>
    <div style="left:60px;top:27px;font-size:8px;color:var(--faint)">Nearest Location</div>
    <div style="left:60px;top:40px;font-size:10px;color:var(--orange);letter-spacing:2px">&#9733;&#9733;&#9733;&#9733;&#9733;</div>
  </div>
  <div class="btn" style="left:74px;top:728px;width:130px">&#128722;&#xFE0E; ADD TO CART</div>
  <div style="left:228px;top:721px;width:28px;height:28px;border-radius:50%;background:var(--teal)"><svg style="left:8px;top:8px;width:12px;height:12px" viewBox="0 0 12 12"><path d="M1 1h10v7H5l-3 3V8H1z" fill="none" stroke="#fff" stroke-width="1.3"/></svg></div>
</section>

<section class="screen" style="left:900px;top:1258px;height:604px">
  <div class="hdr" style="height:140px"></div>
  <svg class="back" viewBox="0 0 12 14"><path d="M8 3L4 7l4 4" stroke="#fff" stroke-width="2" fill="none"/></svg>
  <div class="hdr-title">CHATS</div>
  <div class="card-top" style="top:92px;height:512px"></div>
  <div style="left:21px;top:120px;width:218px;height:58px;border-radius:12px 12px 12px 12px;background:var(--teal);color:#fff;font-size:8.5px;line-height:58px;padding-left:17px">Does this store offer free returns?</div>
  <div style="left:215px;top:131px;width:38px;height:38px;border-radius:50%;background:#fff;border:3px solid var(--teal)"></div>
  <div style="left:199px;top:186px;font-size:8px;color:var(--faint)">20th Sept</div>
  <div style="left:38px;top:223px;width:218px;height:130px;border-radius:12px;background:var(--teal-soft);font-size:8.5px;line-height:17px;color:#666;padding:14px 20px 0 28px">A flat, $10 free for a prepaid shipping label is payable by the customer during the Returns Portal process. A returns tracking link will be emailed to you when you finalise your return.</div>
  <div style="left:21px;top:272px;width:32px;height:32px;border-radius:50%;background:var(--teal)"><div style="left:8px;top:8px;width:16px;height:16px;border-radius:50%;border:2.5px solid #fff"></div></div>
  <div style="left:38px;top:360px;font-size:8px;color:var(--faint)">20th Sept</div>
  <div class="quick" style="left:17px">What size is the model?</div>
  <div class="quick" style="left:153px">How much is express shipping?</div>
  <div style="left:17px;top:547px;width:243px;height:33px;border:1px solid var(--line);border-radius:17px;font-size:10.5px;color:var(--faint);line-height:31px;padding-left:15px">Message</div>
  <svg style="left:236px;top:559px;width:10px;height:10px" viewBox="0 0 10 10"><path d="M1 1l8 4-8 4 1.5-4z" fill="#999"/></svg>
</section>

<!-- ROW 4 -->
<section class="screen" style="left:22px;top:1877px;height:781px">
  <div class="hdr" style="height:140px"></div>
  <svg class="back" viewBox="0 0 12 14"><path d="M8 3L4 7l4 4" stroke="#fff" stroke-width="2" fill="none"/></svg>
  <div class="hdr-title">PRODUCT DETAILS</div>
  <div class="card-top" style="top:92px;height:689px"></div>
  <div class="photo" role="img" aria-label="Product photo of a woman in sporty outfit" style="left:21px;top:120px;width:235px;height:170px"></div>
  <div style="left:21px;top:311px;font-size:14px;color:#333">PRODUCT ITEM</div>
  <div class="pill" style="left:21px;top:334px;width:72px;background:var(--red)"><i></i>30% OFF</div>
  <div class="pill" style="left:101px;top:334px;width:96px;background:var(--teal)"><i></i>Free Shipping</div>
  <div class="pill" style="left:21px;top:358px;width:70px;background:var(--orange)"><i></i>Returns</div>
  <div style="left:21px;top:386px;font-size:14px;font-weight:900;color:var(--teal)">$18.99 <span style="position:static;font-size:8px;font-weight:400;color:var(--faint);text-decoration:line-through">$18.99</span></div>
  <div class="size" style="left:23px">S</div><div class="size" style="left:65px">M</div><div class="size" style="left:107px">L</div><div class="size" style="left:149px">XL</div>
  <div class="dot" style="left:23px;background:var(--red)"></div><div class="dot" style="left:46px;background:#7fd1c7"></div><div class="dot" style="left:69px;background:#3d4a5c"></div>
  <div class="para" style="top:480px">Lorem ipsum odor amet, consectetuer adipiscing elit. Habitasse neque rhoncus lobortis vehicula hendrerit vel dapibus. Urna cursus facilisis senectus pulvinar neque laoreet venenatis. Ex feugiat felis fermentum laoreet class semper? Orci aliquam nulla mus sapien lorem porttitor venenatis nisi quisque. Eleifend elementum sem efficitur lobortis arcu. Turpis ridiculus vestibulum; faucibus adipiscing morbi at platea dictum.</div>
  <div style="left:0;top:0;width:279px;height:781px;background:rgba(60,60,60,.32)"></div>
  <div style="left:0;top:650px;width:279px;height:131px;background:var(--pink);border-radius:16px 16px 0 0">
    <div style="left:21px;top:21px;font-size:14px;font-weight:700;color:#fff">OUT OF STOCK</div>
    <div style="left:21px;top:43px;width:44px;height:2px;background:#fff"></div>
    <div style="left:21px;top:61px;width:240px;font-size:8.5px;line-height:17px;color:#fff">We're sorry, but the item you are trying to add to your cart is currently out of stock. Please check back later, or explore similar items in our store.</div>
  </div>
</section>

<section class="screen" style="left:315px;top:2209px;height:604px">
  <div class="hdr" style="top:40px;height:120px"></div>
  <div class="logobar"><svg class="back" viewBox="0 0 12 14"><path d="M8 3L4 7l4 4" stroke="#222" stroke-width="2" fill="none"/></svg><div class="brand">BrightLoop</div><svg class="user" viewBox="0 0 18 18"><circle cx="9" cy="9" r="8" fill="none" stroke="#222" stroke-width="2"/><circle cx="9" cy="7.5" r="3" fill="#222"/><path d="M4 14c2-3 8-3 10 0" fill="#222"/></svg></div>
  <div class="hdr-title">CART</div>
  <div class="card-top" style="top:94px;height:510px"></div>
  <div class="cart-row" style="top:125px"><div class="thumb" role="img" aria-label="Item thumbnail"></div><div class="nm">Crockery Set</div><div class="meta">Color: Black, Size: 5 Pc.</div><div class="amt">$66.00</div></div>
  <div class="cart-row" style="top:177px"><div class="thumb" role="img" aria-label="Item thumbnail"></div><div class="nm">Crockery Set</div><div class="meta">Color: Black, Size: 5 Pc.</div><div class="amt">$66.00</div></div>
  <div class="cart-row" style="top:229px"><div class="thumb" role="img" aria-label="Item thumbnail"></div><div class="nm">Crockery Set</div><div class="meta">Color: Black, Size: 5 Pc.</div><div class="amt">$66.00</div></div>
  <div class="cart-row" style="top:281px"><div class="thumb" role="img" aria-label="Item thumbnail"></div><div class="nm">Crockery Set</div><div class="meta">Color: Black, Size: 5 Pc.</div><div class="amt">$66.00</div></div>
  <div class="cart-row" style="top:333px"><div class="thumb" role="img" aria-label="Item thumbnail"></div><div class="nm">Crockery Set</div><div class="meta">Color: Black, Size: 5 Pc.</div><div class="amt">$66.00</div></div>
  <div class="cart-row" style="top:385px"><div class="thumb" role="img" aria-label="Item thumbnail"></div><div class="nm">Crockery Set</div><div class="meta">Color: Black, Size: 5 Pc.</div><div class="amt">$66.00</div></div>
  <div class="cart-row" style="top:437px"><div class="thumb" role="img" aria-label="Item thumbnail"></div><div class="nm">Crockery Set</div><div class="meta">Color: Black, Size: 5 Pc.</div><div class="amt">$66.00</div></div>
  <div class="cart-row" style="top:489px"><div class="thumb" role="img" aria-label="Item thumbnail"></div><div class="nm">Crockery Set</div><div class="meta">Color: Black, Size: 5 Pc.</div><div class="amt">$66.00</div></div>
  <div class="nav" style="top:546px">
    <svg style="left:47px;top:11px" viewBox="0 0 16 16"><circle cx="7" cy="7" r="4.5" fill="none" stroke="#444" stroke-width="2"/><path d="M10.5 10.5L14 14" stroke="#444" stroke-width="2"/></svg>
    <div class="item" style="left:10px">Search</div>
    <svg style="left:132px;top:11px" viewBox="0 0 16 16"><path d="M8 1l1.5 4.5L14 7l-4.5 1.5L8 13 6.5 8.5 2 7l4.5-1.5z" fill="#444"/></svg>
    <div class="item" style="left:95px">Recommendations</div>
    <div class="bubble" style="left:208px"><svg viewBox="0 0 16 16"><path d="M1 2h2.5l2 8h7l2-6H5" fill="none" stroke="#fff" stroke-width="1.6"/><circle cx="6.5" cy="13" r="1.4" fill="#fff"/><circle cx="11.5" cy="13" r="1.4" fill="#fff"/></svg></div>
    <div class="item on" style="left:179px">Cart</div>
  </div>
</section>

</body>
</html>
```